General Contractors need a new Crisp updated Card Design

We need a new business card design for our company of 25 years based in Toronto call Holvaster Building Inc. : Our goal is to be the leading commercial contractors in Toronto by providing exceptional value to our clients. We work very hard to deliver professional, quality, service in conjunction with consistent price competitiveness to all of our clients on every single project.

Target Market(s)

Design & Build Clients

Industry/Entity Type

Construction Company

Contact Information for Business Card

Address:
18 North Tamlin Glen Road, Unit 57, Marbrook Vale, ON, K7T 2R9
Office: 905-218-5937

Holvasters Logo
Employee Job Description
Employee Cell Phone #
Employee Email
www.holvaster-example.com

Colors

Designer to choose colors to be used in the design.

Requirements
Must have
• Quote Company Saying:
• "Professional. Quality. Service."
Nice to have
• New Crisp up to date look. simple & fresh ( Not to Busy)
Should not have
• NO BLUE PRINTS ON THE BUSINESS CARDS

```html
<!DOCTYPE html>
<html lang="en">
<head>
<meta charset="utf-8">
<title>Holvaster Building Inc. – Business Card</title>
<link rel="stylesheet" href="https://fonts.googleapis.com/css2?family=Questrial&display=swap">
<style>
  :root {
    --page-bg: #e9eaec;
    --green: #0b4d47;
    --green-light: #2a5a54;
    --green-dark: #084540;
    --white: #ffffff;
    --muted: #c7d6d3;
    --panel: #f6f6f6;
    --rule: rgba(255,255,255,0.14);
    --icon: #8fa8a4;
  }
  * { box-sizing: border-box; margin: 0; padding: 0; }
  html, body { width: 1200px; height: 1200px; overflow: hidden; }
  body {
    background: var(--page-bg);
    font-family: "Questrial", "Century Gothic", sans-serif;
    position: relative;
  }
  .card {
    position: absolute;
    left: 271px;
    width: 658px;
    height: 376px;
    overflow: hidden;
  }
  .card-front {
    top: 154px;
    background: radial-gradient(ellipse at 50% 28%, var(--green-light) 0%, var(--green) 65%, var(--green-dark) 100%);
  }
  .brand {
    position: absolute;
    display: flex;
    align-items: center;
    gap: 12px;
    white-space: nowrap;
  }
  .brand-square { display: block; }
  .card-front .brand {
    left: 0; right: 0; top: 152px;
    justify-content: center;
  }
  .card-front .brand-name { font-size: 30px; color: var(--white); letter-spacing: 0.5px; }
  .card-front .brand-square { width: 40px; height: 40px; background: var(--white); }
  .tagline {
    position: absolute;
    text-align: center;
    white-space: nowrap;
  }
  .card-front .tagline {
    left: 0; right: 0; top: 218px;
    font-size: 14px;
    color: var(--muted);
    letter-spacing: 0.3px;
  }
  .card-front .tagline-rule {
    position: absolute;
    left: 179px; width: 300px; top: 239px; height: 1px;
    background: linear-gradient(90deg, transparent, rgba(255,255,255,0.3), transparent);
  }

  .card-back { top: 663px; background: var(--green); }
  .back-panel {
    position: absolute; left: 0; top: 0; width: 300px; height: 376px;
    background: linear-gradient(160deg, #ffffff 0%, var(--panel) 55%, #ededed 100%);
  }
  .card-back .brand { left: 0; width: 300px; top: 153px; justify-content: center; gap: 9px; }
  .card-back .brand-name { font-size: 19px; color: var(--green); }
  .card-back .brand-square { width: 26px; height: 26px; background: var(--green); }
  .card-back .tagline {
    left: 0; width: 300px; top: 206px;
    font-size: 10.5px; color: var(--green);
  }
  .card-back .tagline-rule {
    position: absolute; left: 65px; width: 170px; top: 223px; height: 1px;
    background: linear-gradient(90deg, transparent, rgba(11,77,71,0.35), transparent);
  }
  .notch { position: absolute; left: 285px; top: 52px; }
  .person { position: absolute; left: 331px; top: 52px; }
  .person-name { font-size: 26px; color: var(--white); font-weight: 700; letter-spacing: 0.2px; }
  .person-role { font-size: 13.5px; color: var(--muted); margin-top: 6px; }
  .contact-list { position: absolute; left: 324px; top: 145px; width: 290px; list-style: none; }
  .contact-item {
    display: flex; align-items: center; gap: 20px;
    height: 33px;
    font-size: 14px; color: var(--white); letter-spacing: 0.3px;
    border-bottom: 1px solid var(--rule);
  }
  .contact-item:last-child { border-bottom: 1px solid var(--rule); height: 36px; }
  .contact-item svg { width: 20px; height: 20px; flex: none; }
  .address {
    position: absolute; left: 324px; top: 274px;
    display: flex; gap: 20px;
    font-size: 14px; line-height: 17px; color: var(--white); letter-spacing: 0.3px;
  }
  .address svg { width: 20px; height: 24px; flex: none; margin-top: 2px; }
</style>
</head>
<body>

<section class="card card-front">
  <div class="brand">
    <span class="brand-square"></span>
    <span class="brand-name">Holvaster Building Inc.</span>
  </div>
  <p class="tagline">PROFESSIONAL. QUALITY. SERVICE.</p>
  <div class="tagline-rule"></div>
</section>

<section class="card card-back">
  <div class="back-panel">
    <div class="brand">
      <span class="brand-square"></span>
      <span class="brand-name">Holvaster Building Inc.</span>
    </div>
    <p class="tagline">PROFESSIONAL. QUALITY. SERVICE.</p>
    <div class="tagline-rule"></div>
  </div>
  <svg class="notch" width="16" height="32" viewBox="0 0 16 32"><polygon points="16,0 0,16 16,32" fill="var(--green)"/></svg>

  <div class="person">
    <p class="person-name">Employee Name</p>
    <p class="person-role">Job Description, ABC</p>
  </div>

  <ul class="contact-list">
    <li class="contact-item">
      <svg viewBox="0 0 24 24"><path d="M6.6 10.8a15 15 0 0 0 6.6 6.6l2.2-2.2a1 1 0 0 1 1-.25 11.4 11.4 0 0 0 3.6.57 1 1 0 0 1 1 1V20a1 1 0 0 1-1 1A17 17 0 0 1 3 4a1 1 0 0 1 1-1h3.5a1 1 0 0 1 1 1c0 1.25.2 2.45.57 3.57a1 1 0 0 1-.25 1z" fill="var(--icon)"/></svg>
      <span>416-730-2864</span>
    </li>
    <li class="contact-item">
      <svg viewBox="0 0 24 24"><rect x="2" y="6" width="20" height="13" fill="var(--icon)"/><polyline points="2,6 12,13 22,6" fill="none" stroke="var(--green)" stroke-width="1.6"/></svg>
      <span>employee@holvaster-example.com</span>
    </li>
    <li class="contact-item">
      <svg viewBox="0 0 24 24" fill="none" stroke="var(--icon)" stroke-width="1.6"><circle cx="12" cy="12" r="9"/><ellipse cx="12" cy="12" rx="4" ry="9"/><line x1="3" y1="12" x2="21" y2="12"/><line x1="12" y1="3" x2="12" y2="21"/></svg>
      <span>www.holvaster-example.com</span>
    </li>
  </ul>

  <div class="address">
    <svg viewBox="0 0 20 24"><path d="M10 1a8 8 0 0 0-8 8c0 6 8 14 8 14s8-8 8-14a8 8 0 0 0-8-8z" fill="var(--icon)"/><circle cx="10" cy="9" r="3" fill="var(--green)"/></svg>
    <p>18 North Tamlin Glen Road, Unit 57,<br>Marbrook Vale, ON, K7T 2R9<br>Office: 905-218-5937</p>
  </div>
</section>

</body>
</html>
```